Basketball Training Facility Flyer Design

We need a killer flyer designed for our brand new state of the art basketball training facility here in Syracuse, Utah. This flyer will be distributed to coaches, parents and players in a large school district in Davis and Weber county, Utah. The purpose of the flyer is to announce the launch of the new facility and to encourage parents, coaches and players to come and try out the facility for a free initial session. We're offering a completely complimentary first training session to introduce customers to the facility at no cost.

We use technology and equipment that is typically found in PLH-level training facilities and gymnasiums. Our website can be found here for some additional information - www.corvanhoopworks.com. Customers can easily book and pay online through our website (the functionality will be done by the time we distribute the completed flyer).

The design needs to highlight the equipment we offer at the facility, because no other basketball training center has the same level of technology we do. We want the flyer to be clean and simple.

Please see must haves for specific details.

The size of the flyer we want to print is 5.75 inches by 9.5 inches.

Target Market(s)

Parents of basketball players of all skill levels age 8-18.

Industry/Entity Type

Training

Requirements
Must have
• Design must include this header: You want to dominate on the court. We have the formula to make that happen.

Design must include this sub header or highlight: Free Introductory Training Session!

The design must include our Logo

The design must include the photos attached of the Rebo, the Jumplora and the Dribtek

Under the the photo of the Rebo 4200 (attached) please include this verbiage:
Game Shots in Game Spots at Game Speed

Under the photo of the Jumplora (see attached) please include this verbiage:
Improve Power, Agility and Speed like Never Before

Under the photo of the Dribtek (attached) please include this verbiage:
Real Time Statistics to Improve Dribble Speed, Accuracy and Right / Left Comparison

Include this verbiage somewhere in the design: Technology Used by PLH and the Best D-1 College Teams

The design must include a strong call to action: Call or Click Now to Schedule A Free Training Session!

The design must include our contact information in easy-to-read font and size (also specifically highlighting the website):

Schedule Online in Less Than 60 Seconds!
Call or Click
801-482-7195
www.corvanhoopworks.com
Nice to have
• For examples of the type of design we like, please see the attached images labeled

Please use stock photos of your preference to go in the flyer (preferably images of youth basketball training or kids in basketball training)

We don't want the flyer to be too cluttered, so please use images at your discretion.

Thank you!

```html
<!DOCTYPE html>
<html lang="en">
<head>
<meta charset="utf-8">
<title>Corvan Hoopworks Academy – Free Training Session Flyer</title>
<link rel="stylesheet" href="https://fonts.googleapis.com/css2?family=Anton&family=Oswald:wght@500;700&display=swap">
<style>
  :root {
    --stage: #161616;
    --flyer-top: #2a2a2a;
    --flyer-bottom: #1c1c1c;
    --orange: #ff6a1a;
    --orange-deep: #e0520c;
    --white: #ffffff;
    --ink: #1a1a1a;
    --silver-light: #f2f2f2;
    --silver-mid: #b9b9b9;
    --silver-dark: #6e6e6e;
    --player-red: #8f1414;
    --player-dark: #141414;
  }
  * { box-sizing: border-box; margin: 0; padding: 0; }
  html, body {
    width: 1200px; height: 800px; overflow: hidden;
    background: var(--stage);
  }
  .flyer {
    position: absolute; left: 370px; top: 20px;
    width: 460px; height: 760px; overflow: hidden;
    background: linear-gradient(180deg, var(--flyer-top), var(--flyer-bottom));
    box-shadow: 0 10px 30px rgba(0,0,0,.6);
    font-family: "Oswald", "Arial Narrow", sans-serif;
  }
  .headline { position: absolute; left: 22px; top: 16px; right: 18px; color: var(--orange); }
  .headline__lead { font-weight: 700; font-size: 22px; line-height: 1.1; }
  .headline__main {
    font-family: "Anton", "Impact", sans-serif; font-weight: 400;
    font-size: 39px; line-height: 1.02; margin-top: 2px;
    text-shadow: 2px 2px 0 var(--ink);
  }
  .equipment {
    position: absolute; left: 18px; right: 18px; top: 136px;
    display: flex; gap: 10px;
  }
  .equipment__card {
    flex: 1; background: var(--white); border: 2px solid var(--orange);
    padding: 5px; height: 150px; display: flex; flex-direction: column;
  }
  .equipment__photo { flex: 1; }
  .equipment__photo--dribble { background: linear-gradient(160deg, #d9dde6, #3d5fae); }
  .equipment__photo--rebo { background: radial-gradient(circle at 45% 55%, #d7681f 0 38%, #f3f3f3 40%); }
  .equipment__photo--jump { background: linear-gradient(160deg, #f4f4f4, #c9c9c9 60%, #b22b20); }
  .equipment__caption {
    font-weight: 700; font-size: 8.5px; line-height: 1.15; color: var(--ink);
    margin-top: 4px; height: 30px;
  }
  .contact { position: absolute; left: 22px; top: 306px; color: var(--orange); }
  .contact__web { font-weight: 700; font-size: 26px; line-height: 1.1; }
  .contact__phone { font-weight: 700; font-size: 24px; line-height: 1.1; }
  .brand {
    position: absolute; left: 22px; top: 392px;
    display: flex; align-items: center; gap: 10px;
  }
  .brand__dot { width: 46px; height: 46px; border-radius: 50%; background: var(--orange-deep); }
  .brand__name { font-weight: 700; font-size: 18px; line-height: 1.05; color: var(--orange); width: 110px; }
  .ball-photo {
    position: absolute; left: 312px; top: 318px; width: 56px; height: 56px; border-radius: 50%;
    background: radial-gradient(circle at 35% 35%, #e98a3c, #a8460f);
  }
  .player-photo {
    position: absolute; left: 170px; top: 400px; width: 290px; height: 296px;
    background: linear-gradient(170deg, var(--player-dark) 0 35%, var(--player-red) 60%, var(--player-dark) 100%);
  }
  .offer-badge {
    position: absolute; left: 330px; top: 388px; width: 112px; height: 112px; border-radius: 50%;
    background: radial-gradient(circle at 35% 30%, var(--silver-light), var(--silver-mid) 60%, var(--silver-dark));
    border: 2px solid var(--silver-light);
    display: flex; align-items: center; justify-content: center; text-align: center;
    font-weight: 700; font-size: 15px; line-height: 1.1; color: var(--ink); padding: 10px;
  }
  .schedule {
    position: absolute; left: 22px; top: 470px; width: 160px;
    font-family: "Anton", "Impact", sans-serif; font-size: 26px; line-height: 1.08;
    color: var(--orange); text-shadow: 2px 2px 0 var(--ink);
  }
  .cta-band {
    position: absolute; left: 0; right: 0; top: 700px; height: 40px;
    background: linear-gradient(180deg, var(--silver-light), var(--silver-mid) 55%, var(--silver-dark));
    border-top: 2px solid var(--silver-light); border-bottom: 2px solid var(--silver-dark);
    display: flex; align-items: center; justify-content: center;
    font-weight: 700; font-size: 17px; color: var(--ink);
  }
</style>
</head>
<body>
  <main class="flyer">
    <header class="headline">
      <p class="headline__lead">You want to dominate on the court.</p>
      <h1 class="headline__main">We have the formula to<br>make that happen.</h1>
    </header>

    <section class="equipment">
      <figure class="equipment__card">
        <div class="equipment__photo equipment__photo--dribble" role="img" aria-label="Young player training on the Dribtek dribble mat"></div>
        <figcaption class="equipment__caption">Real Time Statistics to Improve Dribble Speed, Accuracy and Right / Left Comparison</figcaption>
      </figure>
      <figure class="equipment__card">
        <div class="equipment__photo equipment__photo--rebo" role="img" aria-label="Smart basketball with phone showing shot data"></div>
        <figcaption class="equipment__caption">Game Shots in Game Spots at Game Speed</figcaption>
      </figure>
      <figure class="equipment__card">
        <div class="equipment__photo equipment__photo--jump" role="img" aria-label="Jumplora power and agility training machine"></div>
        <figcaption class="equipment__caption">Improve Power, Agility and Speed like Never Before</figcaption>
      </figure>
    </section>

    <div class="contact">
      <p class="contact__web">www.corvanhoopworks.com</p>
      <p class="contact__phone">801-482-7195</p>
    </div>

    <div class="ball-photo" role="img" aria-label="Basketball"></div>

    <div class="brand">
      <span class="brand__dot"></span>
      <span class="brand__name">Corvan Hoopworks Academy</span>
    </div>

    <div class="player-photo" role="img" aria-label="Player in red shorts driving to the basket"></div>

    <p class="offer-badge">Free Introductory Training Session!</p>

    <p class="schedule">Schedule Online in Less Than 60 Seconds! Call or Click</p>

    <p class="cta-band">Call or Click Now to Schedule A Free Training Session!</p>
  </main>
</body>
</html>
```